Edible insect info graphic banner design

We need an info graphic that will be used to show why edible insects are so great for the environment! More pictures and less words. Preferred design would include our "superbug" and/or animated farm animals from previous design project (see attached).

Final design should have "environmental" "save the planet" feel

The winning design will include more images to describe the following points, instead if words. Size will be as per pop up banner artwork requirements in attached image (2000mm (h) x 850mm (w))

1. Include our logo

2 . Include our website CrunchyMealHall.com.au

3. Title of info graphic "why we should eat more bugs"

4. Take up little space to breed. Crates of edible insects such as crickets can be stacked on top of each other like bug apartments

5. Insects are a sustainable source of protein. High in protein, calcium, iron and amino acids, and are also low in saturated fats.

6. They taste delicious and versatile

7. 100g beef requires 2000L water, 1000g feed and creates 285g CO2.
100g cricket requires 10ml water, 90g feed and creates 0.2g CO2

8. over 80% of the world population already eats edible insects

9. by eating insects one day per week, you save over 162,000L water per year

See our website for more inspiration

Industry/Entity Type

Farm

Colors
ffffff
9bcb3c
cadf82
fbf289
faed22
33a6d7

Requirements
Must have
• Simple design, clean and clear imagery

Flexible on colours

```html
<!DOCTYPE html>
<html lang="en">
<head>
<meta charset="utf-8">
<title>Why We Should Eat More Bugs – Pop-up Banner</title>
<link rel="stylesheet" href="https://fonts.googleapis.com/css2?family=Bebas+Neue&family=Comfortaa:wght@400;700&family=Josefin+Sans:wght@400;600;700&display=swap">
<style>
  :root {
    --sky-top: #4ccbf1;
    --sky-mid: #8fdcf5;
    --sky-pale: #e6f8fd;
    --white: #ffffff;
    --lime: #9bdc1c;
    --lime-dark: #7fbf10;
    --ocean: #33a6d7;
    --ocean-deep: #1f7fb0;
    --hero-navy: #1c2b6e;
    --cape-olive: #8a7f3a;
    --frame: #1a1a1a;
    --pointer: #111111;
  }
  * { margin: 0; padding: 0; box-sizing: border-box; }
  html, body { width: 1200px; height: 1000px; overflow: hidden; background: var(--white); }
  .canvas { position: relative; width: 1200px; height: 1000px; }

  /* Banner */
  .banner {
    position: absolute; left: 72px; top: 83px; width: 358px; height: 838px;
    border: 1.5px solid var(--frame);
    background: linear-gradient(180deg, var(--sky-top) 0%, var(--sky-mid) 40%, var(--sky-pale) 64%, var(--white) 76%);
    overflow: hidden; text-align: center; color: var(--white);
  }
  .banner__title {
    position: absolute; left: 0; right: 0; top: 34px;
    font-family: "Bebas Neue", sans-serif; font-weight: 400;
    font-size: 52px; line-height: 52px; letter-spacing: 1px;
  }
  .banner__title-bugs {
    display: block; margin-top: 4px;
    font-family: "Comfortaa", sans-serif; font-weight: 400;
    font-size: 76px; line-height: 76px; letter-spacing: 2px;
    color: var(--white); -webkit-text-stroke: 3px var(--lime);
  }
  .grass {
    position: absolute; top: 135px; width: 36px; height: 80px;
    background: linear-gradient(180deg, rgba(255,255,255,0.1), rgba(255,255,255,0.85));
    border-radius: 50% 50% 4px 4px / 100% 100% 4px 4px;
  }
  .grass--left { left: 24px; }
  .grass--right { right: 24px; }

  .facts {
    position: absolute; left: 0; right: 0; top: 247px;
    font-family: "Josefin Sans", sans-serif; font-size: 8.4px; line-height: 11px; text-transform: uppercase;
  }
  .facts p { margin-bottom: 20px; }
  .facts .fact--crates { margin-bottom: 26px; }
  .facts .fact--taste { margin-bottom: 22px; }
  .facts .fact--water { margin-bottom: 24px; }
  .facts .fact--stat { font-weight: 600; font-size: 8.4px; line-height: 11px; color: var(--white); text-shadow: 0 0 3px rgba(31,127,176,0.45); }

  .worldwide {
    position: absolute; left: 16px; top: 500px; width: 158px;
    display: flex; align-items: center; gap: 8px; text-align: left;
    font-family: "Josefin Sans", sans-serif; font-weight: 600; font-size: 8.4px; line-height: 11px;
    text-transform: uppercase; color: var(--ocean-deep);
  }
  .worldwide__pie { flex: none; }
  .worldwide__figure { display: block; font-family: "Bebas Neue", sans-serif; font-size: 24px; line-height: 22px; color: var(--lime-dark); }

  .compare {
    position: absolute; left: 16px; top: 572px; width: 158px; text-align: left;
    font-family: "Josefin Sans", sans-serif; text-transform: uppercase; color: var(--ocean-deep);
  }
  .compare__title { font-weight: 700; font-size: 8.4px; line-height: 11px; margin-bottom: 6px; }
  .compare__chart { display: block; }
  .compare__chart text { font-family: "Josefin Sans", sans-serif; font-size: 8px; font-weight: 600; fill: var(--ocean-deep); }

  .superbug {
    position: absolute; left: 178px; top: 497px; width: 180px; height: 290px;
    background: linear-gradient(160deg, var(--hero-navy) 0%, #24338a 45%, var(--cape-olive) 100%);
    border-radius: 60px 60px 10px 10px; opacity: 0.9;
  }
  .brand {
    position: absolute; left: 26px; top: 728px; width: 140px;
    display: flex; align-items: center; gap: 6px;
    font-family: "Comfortaa", sans-serif; font-weight: 700; font-size: 15px; line-height: 17px;
    color: var(--lime-dark); text-align: left;
  }
  .brand__dot { width: 12px; height: 12px; border-radius: 50%; background: var(--lime-dark); flex: none; }
  .banner__url {
    position: absolute; left: 0; right: 0; bottom: 14px;
    font-family: "Comfortaa", sans-serif; font-weight: 700; font-size: 25px; color: var(--lime);
  }

  /* Magnified detail */
  .pointer { position: absolute; left: 0; top: 0; }
  .zoom {
    position: absolute; left: 576px; top: 40px; width: 594px; height: 594px;
    border-radius: 50%; border: 3px solid #2b2b2b; overflow: hidden;
    background: linear-gradient(180deg, var(--sky-top) 0%, var(--sky-mid) 50%, var(--sky-pale) 82%, var(--white) 100%);
    text-align: center; color: var(--white);
  }
  .zoom__bugs {
    position: absolute; left: 0; right: 0; top: -96px;
    font-family: "Comfortaa", sans-serif; font-size: 130px; line-height: 130px; letter-spacing: 4px;
    -webkit-text-stroke: 5px var(--lime);
  }
  .zoom__facts {
    position: absolute; left: 0; right: 0; top: 95px;
    font-family: "Josefin Sans", sans-serif; font-size: 14px; line-height: 19px; text-transform: uppercase;
  }
  .zoom__facts p { margin-bottom: 39px; }
  .zoom__facts .fact--stat { font-weight: 600; font-size: 13px; line-height: 18px; text-shadow: 0 0 4px rgba(31,127,176,0.5); }
  .zoom__worldwide {
    position: absolute; left: 110px; top: 498px; width: 300px;
    display: flex; align-items: center; gap: 12px; text-align: left;
    font-family: "Josefin Sans", sans-serif; font-weight: 600; font-size: 14px; line-height: 18px;
    text-transform: uppercase; color: var(--ocean-deep);
  }
  .zoom__worldwide .worldwide__figure { font-size: 38px; line-height: 34px; }
  .zoom__hero {
    position: absolute; left: 420px; top: 520px; width: 110px; height: 110px;
    border-radius: 50% 50% 0 0; background: linear-gradient(180deg, var(--hero-navy), #24338a);
  }
</style>
</head>
<body>
<main class="canvas">
  <section class="banner">
    <div class="grass grass--left" role="img" aria-label="Decorative grass tufts"></div>
    <div class="grass grass--right" role="img" aria-label="Decorative grass tufts"></div>
    <h1 class="banner__title">Why we should<br>eat more<span class="banner__title-bugs">BUGS</span></h1>
    <div class="facts">
      <p>Insects are a sustainable source of protein.<br>High in protein, calcium, iron and amino acids,<br>and are also low in saturated fats!</p>
      <p class="fact--crates">Insects take up little space to breed and<br>crates of edible insects such as crickets<br>can be stacked on top of each other like bug apartments</p>
      <p class="fact--taste">They taste delicious and versatile</p>
      <p class="fact--water">By eating insects one day per week, you save over<br>162,000L water per year</p>
      <p class="fact--stat">100g beef requires 2000L water, 1000g feed and creates 285g CO2.<br>100g cricket requires 10ml water, 90g feed and creates 0.2g CO2</p>
    </div>

    <div class="worldwide">
      <svg class="worldwide__pie" width="44" height="44" viewBox="0 0 44 44" aria-hidden="true">
        <circle cx="22" cy="22" r="20" fill="var(--white)"/>
        <circle cx="22" cy="22" r="10" fill="none" stroke="var(--lime)" stroke-width="20"
                stroke-dasharray="50.27 62.83" transform="rotate(-90 22 22)"/>
      </svg>
      <p><span class="worldwide__figure">80%+</span>of the world population already eats insects</p>
    </div>

    <div class="compare">
      <p class="compare__title">Water per 100g</p>
      <svg class="compare__chart" width="158" height="52" viewBox="0 0 158 52" role="img" aria-label="Bar chart: beef needs 2000 litres of water per 100g, crickets need 10 millilitres">
        <text x="0" y="12">Beef</text>
        <rect x="44" y="3" width="110" height="12" rx="2" fill="var(--ocean)"/>
        <text x="0" y="34">Cricket</text>
        <rect x="44" y="25" width="4" height="12" rx="1" fill="var(--lime-dark)"/>
        <text x="52" y="34">10ml</text>
        <text x="118" y="50">2000L</text>
      </svg>
    </div>

    <div class="superbug" role="img" aria-label="Superbug mascot: insect superhero in navy suit and olive cape"></div>
    <div class="brand"><span class="brand__dot"></span><span>Crunchy<br>Meal Hall</span></div>
    <p class="banner__url">CrunchyMealHall.com.au</p>
  </section>

  <svg class="pointer" width="1200" height="1000" aria-hidden="true">
    <line x1="392" y1="472" x2="592" y2="420" stroke="var(--pointer)" stroke-width="6" stroke-linecap="round"/>
  </svg>

  <section class="zoom">
    <div class="zoom__bugs" aria-hidden="true">BUGS</div>
    <div class="zoom__facts">
      <p>Insects are a sustainable source of protein.<br>High in protein, calcium, iron and amino acids,<br>and are also low in saturated fats!</p>
      <p>Insects take up little space to breed and<br>crates of edible insects such as crickets<br>can be stacked on top of each other like bug apartments</p>
      <p>They taste delicious and versatile</p>
      <p>By eating insects one day per week, you save over<br>162,000L water per year</p>
      <p class="fact--stat">100g beef requires 2000L water, 1000g feed and creates 285g CO2.<br>100g cricket requires 10ml water, 90g feed and creates 0.2g CO2</p>
    </div>
    <div class="zoom__worldwide">
      <svg class="worldwide__pie" width="64" height="64" viewBox="0 0 44 44" aria-hidden="true">
        <circle cx="22" cy="22" r="20" fill="var(--white)"/>
        <circle cx="22" cy="22" r="10" fill="none" stroke="var(--lime)" stroke-width="20"
                stroke-dasharray="50.27 62.83" transform="rotate(-90 22 22)"/>
      </svg>
      <p><span class="worldwide__figure">80%+</span>of the world population already eats insects</p>
    </div>
    <div class="zoom__hero" role="img" aria-label="Top of the superbug mascot's head"></div>
  </section>
</main>
</body>
</html>
```